Open Now Poster for Retail Shop windows.

To design a poster to be printed to put on the windows of our retail stores to tell customers that we are open. Size is to be 590mm W x 840mm H supplied as a pdf. Design should incorporate our logo as well as other elements which indicate the style of our shop which is Womens Beach, Resort & Casual Clothing, Swimwear and Accessories. I would like the design to incorporate the words "Open Now" in some form in large lettering. I would also like the poster to be timeless and able to be used for other wording, so no images would be preferable.

Target Market(s)

Womens Beach, Resort & Casual Clothing, Swimwear and Accessories

Industry/Entity Type

Retail

Colors
e34297

Requirements
Must have
• words "Open Now". as well as our logo.

```html
<!DOCTYPE html>
<html lang="en">
<head>
<meta charset="utf-8">
<title>Open Now – Window Poster</title>
<link rel="stylesheet" href="https://fonts.googleapis.com/css2?family=Oswald:wght@600&family=Nunito:wght@700&display=swap">
<style>
  :root {
    --stage: #ece8ea;
    --pink-light: #e0399a;
    --pink-deep: #c8135b;
    --aqua: #35e3e8;
    --white: #ffffff;
    --figure-warm: #d9a07e;
    --figure-denim: #9fb3c8;
  }
  html, body {
    margin: 0;
    padding: 0;
    width: 1200px;
    height: 900px;
    overflow: hidden;
    background: var(--stage);
  }
  .canvas {
    position: relative;
    width: 1200px;
    height: 900px;
    display: flex;
    align-items: center;
    justify-content: center;
  }
  .poster {
    position: relative;
    width: 604px;
    height: 860px;
    overflow: hidden;
    box-shadow: 0 6px 24px rgba(0,0,0,0.18);
  }
  .poster-bg {
    position: absolute;
    inset: 0;
    width: 100%;
    height: 100%;
  }
  .poster-frame {
    position: absolute;
    inset: 20px;
    border: 2px solid var(--white);
  }
  .brand {
    position: absolute;
    top: 38px;
    left: 38px;
    font-family: "Nunito", sans-serif;
    font-weight: 700;
    font-size: 22px;
    color: var(--white);
    letter-spacing: 0.5px;
  }
  .headline {
    position: absolute;
    top: 70px;
    left: 150px;
    padding: 2px 22px 6px;
    border: 5px solid var(--aqua);
    font-family: "Oswald", sans-serif;
    font-weight: 600;
    font-size: 84px;
    line-height: 1;
    color: var(--aqua);
    text-transform: uppercase;
    letter-spacing: 1px;
    margin: 0;
  }
  .figure-art {
    position: absolute;
    top: 200px;
    left: 250px;
    width: 300px;
    height: 620px;
    border-radius: 140px 140px 60px 60px;
    background: linear-gradient(180deg, rgba(160,60,40,0.35) 0%, rgba(217,160,126,0.45) 35%, rgba(159,179,200,0.45) 55%, rgba(217,160,126,0.4) 75%, rgba(150,90,40,0.45) 100%);
  }
</style>
</head>
<body>
  <main class="canvas">
    <section class="poster">
      <svg class="poster-bg" viewBox="0 0 604 860" preserveAspectRatio="none" aria-hidden="true">
        <rect width="604" height="860" fill="var(--pink-deep)"/>
        <polygon points="0,0 604,0 40,860 0,860" fill="var(--pink-light)"/>
      </svg>
      <div class="poster-frame"></div>
      <div class="brand">sea sol</div>
      <h1 class="headline">Open Now</h1>
      <div class="figure-art" role="img" aria-label="Illustration of a woman with long red hair in a white knotted top, denim shorts and brown boots"></div>
    </section>
  </main>
</body>
</html>
```